new website design for cloud communications company

started building a new site but dont have enough time to finish
http://plixo47.sitebuildr.net/music-studio-mp

you can also use content from our current website www.korvanasolutions-demo.com

would also like to be mobile optimized if possible, and wix compatible

please submit a logo design with website =) project is guaranteed

Industry/Entity Type

Telecommunications

Logo Text

Korvana Solutions redefining cloud communications

Number of Pages Required

5+ page

Requirements
Must have
• 1.pricing table comparable to this: http://www.talvoquay-demo.com/office/plansandpricing.html
• 2. terms of service link
• 3. portals drop down like on the new site with the korvana 2 portal opening inside the site similar to setup on new site shown
• 4. modern look

```html
<!DOCTYPE html>
<html lang="en">
<head>
<meta charset="utf-8">
<title>Korvana Solutions — Recording Studio</title>
<link href="https://fonts.googleapis.com/css2?family=Source+Sans+3:ital,wght@0,300;0,400;0,600;1,300;1,400;1,600&display=swap" rel="stylesheet">
<style>
:root{
  --teal:#74c3cc;
  --teal-deep:#2a93a3;
  --teal-dark:#1f7f8c;
  --hero-pale:#c3e3e7;
  --hero-mid:#8fcbd1;
  --hero-strong:#33b0bd;
  --grey-band:#dedcdd;
  --grey-text:#8a8a8a;
  --light-text:#b9b9b9;
  --white:#ffffff;
}
*{margin:0;padding:0;box-sizing:border-box}
html,body{width:1200px;height:2956px;overflow:hidden}
body{position:relative;background:var(--white);font-family:"Source Sans 3",sans-serif;color:var(--grey-text)}
.abs{position:absolute}
.hero{left:0;top:0;width:1200px;height:655px;
  background:
    radial-gradient(ellipse 340px 300px at 340px 300px,rgba(120,150,160,.35),transparent 70%),
    radial-gradient(ellipse 300px 260px at 720px 180px,rgba(200,210,190,.35),transparent 70%),
    linear-gradient(100deg,var(--hero-pale) 0%,var(--hero-mid) 40%,var(--hero-strong) 75%,#2ea9b6 100%)}
.nav{left:0;top:600px;width:1200px;height:55px;background:rgba(42,160,172,.75);display:flex;justify-content:center;align-items:center}
.nav a{color:var(--white);text-decoration:none;font-size:13px;padding:0 22px;line-height:55px;border-right:1px solid rgba(255,255,255,.25)}
.nav a:last-child{border-right:0}
.section-title{left:0;width:1200px;text-align:center;color:var(--teal-deep);font-size:22px;font-weight:400}
.service{width:260px;text-align:center}
.service svg{display:block;margin:0 auto}
.service h3{margin-top:8px;color:var(--teal-dark);font-size:17px;font-style:italic;font-weight:600;letter-spacing:.5px}
.service p{margin:14px auto 0;width:170px;font-size:11px;line-height:16px;color:var(--light-text)}
.btn{display:inline-flex;align-items:center;justify-content:center;gap:5px;font-size:12px;text-transform:uppercase;border:1px solid var(--teal);color:var(--teal);background:var(--white);height:28px;width:112px;margin-top:30px;white-space:nowrap}
.btn.solid{background:var(--teal);color:var(--white)}
.hello{left:0;top:1100px;width:1200px;height:151px;background:var(--grey-band);text-align:center;padding-top:33px;font-size:20px;font-style:italic;color:#7a7a7a}
.welcome{left:0;top:1251px;width:1200px;height:130px;background:var(--teal);color:var(--white);padding:30px 142px 0}
.welcome h2{font-size:21px;font-style:italic;font-weight:400}
.welcome p{margin-top:6px;font-size:11px;font-style:italic;line-height:17px;width:820px}
.works-title{top:1428px;font-style:italic;text-transform:uppercase;font-size:20px;color:var(--teal)}
.work{width:140px;text-align:center;top:1488px}
.work .disc{width:98px;height:98px;border-radius:50%;border:2px solid var(--teal);margin:0 auto;padding:4px}
.work .disc span{display:flex;width:100%;height:100%;border-radius:50%;background:radial-gradient(circle at 40% 35%,#a6d9de,#63b7c1);align-items:center;justify-content:center}
.work .disc span.warm{background:radial-gradient(circle at 50% 40%,#8a7566,#4b3c35)}
.work .name{margin-top:6px;font-size:15px;font-style:italic;line-height:16px;color:var(--teal)}
.view-all{left:545px;top:1667px;width:110px;height:36px;background:var(--teal);color:var(--white);font-size:15px;font-style:italic;display:flex;align-items:center;justify-content:center}
.about{left:0;top:1781px;width:1200px;height:343px;background:var(--teal);color:var(--white)}
.about h2{position:absolute;top:58px;width:1200px;text-align:center;font-size:19px;font-style:italic;font-weight:400}
.about .avatar{position:absolute;left:92px;top:87px;width:150px;height:150px;border-radius:50%;border:3px solid var(--white);background:radial-gradient(circle at 45% 40%,#b94d4d,#5a1f22 60%,#2a1416)}
.about p{position:absolute;left:258px;top:125px;width:820px;font-size:14px;font-style:italic;line-height:22px}
.contact-title{left:142px;top:2165px;font-size:20px;font-style:italic;font-weight:400;color:var(--light-text)}
.ready{left:142px;top:2205px;font-size:15px;color:var(--grey-text)}
.call{left:142px;top:2236px;font-size:11px;line-height:17px;color:var(--light-text)}
.map{left:144px;top:2289px;width:354px;height:270px;
  background:
    radial-gradient(ellipse 120px 80px at 80px 200px,rgba(170,190,140,.45),transparent 70%),
    radial-gradient(ellipse 140px 90px at 280px 60px,rgba(200,200,160,.5),transparent 70%),
    linear-gradient(135deg,#cfc9b6,#bdb7a3 50%,#c9c3ae)}
.get-voip{left:421px;top:2565px;width:77px;height:26px;background:var(--teal);color:var(--white);font-size:14px;display:flex;align-items:center;justify-content:center}
.field{left:764px;width:294px;height:34px;border:1px solid var(--teal);font-size:11px;color:var(--light-text);padding:8px 6px}
.field.message{height:124px}
.info{left:569px;top:2660px;width:398px;height:171px;background:var(--teal);color:var(--white);font-size:11px;line-height:19px;font-style:normal}
.info .col-left{position:absolute;left:18px;top:24px;display:flex;gap:10px}
.info .col-right{position:absolute;left:212px;top:48px;font-size:10.5px}
.info .divider{position:absolute;left:201px;top:10px;width:1px;height:150px;background:rgba(255,255,255,.7)}
.info .row{display:flex;align-items:center;gap:7px;white-space:nowrap}
.footer{left:0;top:2908px;width:1200px;height:48px;background:var(--teal);color:var(--white);font-size:11px;padding-left:83px;line-height:48px;word-spacing:2px;white-space:nowrap}
</style>
</head>
<body>

<div class="abs hero" role="img" aria-label="Photo of a person with earphones using a smartphone, tinted teal"></div>
<nav class="abs nav">
  <a href="#">Home</a><a href="#">Plans &amp; Pricing</a><a href="#">Phone</a><a href="#">Services</a><a href="#">White Label Hosted PBX</a><a href="#">Portals</a>
</nav>

<h2 class="abs section-title" style="top:704px">Our Services</h2>

<div class="abs service" style="left:79px;top:770px">
  <svg width="104" height="140" viewBox="0 0 104 140"><path d="M52 2C24 2 2 24 2 52c0 34 50 86 50 86s50-52 50-86C102 24 80 2 52 2z" fill="var(--teal)"/><circle cx="52" cy="52" r="38" fill="#fff"/><rect x="45" y="28" width="14" height="28" rx="7" fill="none" stroke="#222" stroke-width="3"/><path d="M39 48c0 10 6 16 13 16s13-6 13-16M52 64v10" fill="none" stroke="#222" stroke-width="3"/></svg>
  <h3>Recording</h3>
  <p>sentence structures, to generate which looks reasonable</p>
  <span class="btn"><svg width="11" height="13" viewBox="0 0 11 13"><rect x="1" y="1" width="9" height="11" fill="none" stroke="currentColor"/></svg>More info</span>
</div>

<div class="abs service" style="left:441px;top:770px">
  <svg width="104" height="140" viewBox="0 0 104 140"><path d="M52 2C24 2 2 24 2 52c0 34 50 86 50 86s50-52 50-86C102 24 80 2 52 2z" fill="var(--teal)"/><circle cx="52" cy="52" r="38" fill="#fff"/><circle cx="50" cy="52" r="25" fill="#d9d9d9" stroke="#9a9a9a"/><circle cx="50" cy="52" r="5" fill="#fff" stroke="#888"/><path d="M62 40v22" stroke="#5b4bb0" stroke-width="3"/><circle cx="58" cy="63" r="5" fill="#5b4bb0"/></svg>
  <h3>Mp3</h3>
  <p>Contrary to popular belief, Lorem is not simply random text. It has</p>
  <span class="btn solid"><svg width="11" height="13" viewBox="0 0 11 13"><rect x="1" y="1" width="9" height="11" fill="none" stroke="currentColor"/></svg>More info</span>
</div>

<div class="abs service" style="left:828px;top:770px">
  <svg width="104" height="140" viewBox="0 0 104 140"><path d="M52 2C24 2 2 24 2 52c0 34 50 86 50 86s50-52 50-86C102 24 80 2 52 2z" fill="var(--teal)"/><circle cx="52" cy="52" r="38" fill="#fff"/><rect x="28" y="36" width="48" height="32" fill="#fff" stroke="#111" stroke-width="3"/><g fill="#111"><rect x="33" y="36" width="5" height="19"/><rect x="42" y="36" width="5" height="19"/><rect x="52" y="36" width="5" height="19"/><rect x="61" y="36" width="5" height="19"/><rect x="69" y="36" width="5" height="19"/></g></svg>
  <h3>Piano</h3>
  <p>The majority have suffered alteration in by injected humour</p>
  <span class="btn"><svg width="11" height="13" viewBox="0 0 11 13"><rect x="1" y="1" width="9" height="11" fill="none" stroke="currentColor"/></svg>More info</span>
</div>

<div class="abs hello">HELLO THERE!</div>

<section class="abs welcome">
  <h2>WELCOME TO OUR RECORDING STUDIO</h2>
  <p>avoids pleasure itself, because it is pleasure, but because those who do not know how to pursue pleasure rationally encounter consequences that are extremely painful. Nor again is there anyone who loves or pursues or desires to obtain pain of itself, because it is pain</p>
</section>

<h2 class="abs section-title works-title">Feature Works</h2>

<div class="abs work" style="left:147px"><div class="disc"><span role="img" aria-label="Artist photo with play button"><svg width="34" height="34" viewBox="0 0 34 34"><circle cx="17" cy="17" r="15" fill="none" stroke="#fff" stroke-width="2"/><path d="M13 10l11 7-11 7z" fill="#fff"/></svg></span></div><div class="name">Mira<br>Tolland</div></div>
<div class="abs work" style="left:287px"><div class="disc"><span role="img" aria-label="Artist photo with play button"><svg width="34" height="34" viewBox="0 0 34 34"><circle cx="17" cy="17" r="15" fill="none" stroke="#fff" stroke-width="2"/><path d="M13 10l11 7-11 7z" fill="#fff"/></svg></span></div><div class="name">Jory<br>Penn</div></div>
<div class="abs work" style="left:424px"><div class="disc"><span role="img" aria-label="Artist photo with play button"><svg width="34" height="34" viewBox="0 0 34 34"><circle cx="17" cy="17" r="15" fill="none" stroke="#fff" stroke-width="2"/><path d="M13 10l11 7-11 7z" fill="#fff"/></svg></span></div><div class="name">Cal<br>Brewin</div></div>
<div class="abs work" style="left:561px"><div class="disc"><span role="img" aria-label="Artist photo with play button"><svg width="34" height="34" viewBox="0 0 34 34"><circle cx="17" cy="17" r="15" fill="none" stroke="#fff" stroke-width="2"/><path d="M13 10l11 7-11 7z" fill="#fff"/></svg></span></div><div class="name">Nessa<br>Varro</div></div>
<div class="abs work" style="left:706px"><div class="disc"><span role="img" aria-label="Artist photo with play button"><svg width="34" height="34" viewBox="0 0 34 34"><circle cx="17" cy="17" r="15" fill="none" stroke="#fff" stroke-width="2"/><path d="M13 10l11 7-11 7z" fill="#fff"/></svg></span></div><div class="name">Tova<br>Rell</div></div>
<div class="abs work" style="left:848px"><div class="disc"><span class="warm" role="img" aria-label="Artist photo with play button"><svg width="34" height="34" viewBox="0 0 34 34"><circle cx="17" cy="17" r="15" fill="none" stroke="#fff" stroke-width="2"/><path d="M13 10l11 7-11 7z" fill="#fff"/></svg></span></div><div class="name">Owen<br>Hask</div></div>

<div class="abs view-all">VIEW ALL</div>

<section class="abs about">
  <h2>SHORTLY ABOUT US</h2>
  <div class="avatar" role="img" aria-label="Photo of a singer performing with a microphone"></div>
  <p>occasionally circumstances occur in which toil and pain can procure him some great pleasure. To take a trivial example, which of us ever undertakes laborious physical exercise, except to obtain some advantage from it? But who has any right to find fault with a man who chooses to enjoy a pleasure that has no annoying consequences, or one who avoids a pain that produces no resultant pleasure?"</p>
</section>

<h2 class="abs contact-title">SHORTLY ABOUT US</h2>
<p class="abs ready">Ready to learn more?</p>
<p class="abs call">Call us toll free at 1-855-korvana<br>or fill out the contact form &amp; we'll get you rolling.</p>
<div class="abs map" role="img" aria-label="Street map of the office area with red location pins"></div>
<div class="abs get-voip">GET VOIP</div>

<div class="abs field" style="top:2291px">Name</div>
<div class="abs field" style="top:2332px">Email</div>
<div class="abs field" style="top:2374px">Phone</div>
<div class="abs field" style="top:2415px">Subject</div>
<div class="abs field message" style="top:2453px">Message</div>

<address class="abs info">
  <div class="col-left">
    <svg width="14" height="18" viewBox="0 0 14 18"><path d="M7 1C3.7 1 1 3.6 1 6.9 1 11 7 17 7 17s6-6 6-10.1C13 3.6 10.3 1 7 1z" fill="#fff"/><circle cx="7" cy="7" r="2.3" fill="var(--teal)"/></svg>
    <div>TECHNICAL SERVICES<br>&nbsp;&nbsp;&nbsp;42 ROUTE 9W<br>&nbsp;&nbsp;&nbsp;FERNHOLLOW, NJ 07999<br>&nbsp;&nbsp;&nbsp;BILLING DEPARTMENT<br>&nbsp;&nbsp;&nbsp;880-2 BIRCHLINE RD<br>&nbsp;&nbsp;&nbsp;OAK TARN, NJ 07998</div>
  </div>
  <div class="divider"></div>
  <div class="col-right">
    <div class="row"><svg width="14" height="10" viewBox="0 0 14 10"><rect width="14" height="10" fill="#fff"/><path d="M0 0l7 5 7-5" fill="none" stroke="var(--teal)"/></svg>sales@korvanasolutions-demo.com</div>
    <div class="row"><svg width="14" height="14" viewBox="0 0 14 14"><path d="M3 1l3 3-2 2c1 2 2 3 4 4l2-2 3 3-2 2C6 13 1 8 1 3z" fill="#fff"/></svg>Tel: 1-855-KORVANA</div>
    <div class="row"><svg width="14" height="12" viewBox="0 0 14 12"><rect x="3" y="0" width="8" height="4" fill="#fff"/><rect x="0" y="4" width="14" height="6" fill="#fff"/><rect x="3" y="8" width="8" height="4" fill="#fff" stroke="var(--teal)"/></svg>Fax: 555-014-2290</div>
  </div>
</address>

<footer class="abs footer">©2015 by Korvana Solutions LLP. &nbsp;&nbsp; 855 korvana1 sales@korvanasolutions-demo.com, &nbsp;&nbsp; 42 Route 9W bldg., &nbsp;&nbsp; Esuit 36 Fernhollow, NJ 07999</footer>

</body>
</html>
```